Business Card, Stationary with Shark Logo for Personal Injury Lawyer

I need business cards and stationery with a shark logo for my Personal Injury Law Practice. Has to have this written on it:
Martin K. Hollis
Injury Lawyer
The Corvell Building
718 Tandy Street
Providence, Rhode Island 02908
401-627-4193
Martinhollis.com

Contact Information for Business Card

Martin K. Hollis, Injury Lawyer, address, 401-627-4193, martinhollis.com

```html
<!DOCTYPE html>
<html lang="en">
<head>
<meta charset="utf-8">
<title>Martin K. Hollis — Business Card</title>
<link href="https://fonts.googleapis.com/css2?family=Montserrat:wght@500;800&display=swap" rel="stylesheet">
<style>
  :root {
    --backdrop: #2b2e33;
    --card-navy: #2a2268;
    --card-white: #ffffff;
    --ink-navy: #2a2268;
    --ink-text: #1f2a5c;
    --icon-blue: #3d5fc0;
    --rule: #1f2a5c;
  }
  * { box-sizing: border-box; margin: 0; padding: 0; }
  html, body {
    width: 1200px; height: 1000px; overflow: hidden;
    background: var(--backdrop);
    font-family: "Montserrat", sans-serif;
  }
  .sheet {
    width: 1200px; height: 1000px;
    display: flex; flex-direction: column; align-items: center;
    justify-content: center; gap: 28px;
  }
  .card {
    width: 780px; height: 446px;
    border-radius: 26px;
    position: relative;
    box-shadow: 0 14px 30px rgba(0,0,0,.35);
  }
  .card--front {
    background: var(--card-navy);
    display: flex; align-items: center; justify-content: center;
  }
  .card--back {
    background: var(--card-white);
    display: flex; align-items: center;
    padding: 0 50px 0 60px;
  }
  .brand { display: flex; flex-direction: column; }
  .card--front .brand { align-items: center; }
  .brand-name {
    font-weight: 800;
    text-transform: uppercase;
    line-height: 1;
  }
  .brand-tagline {
    font-weight: 800;
    text-transform: uppercase;
    line-height: 1;
    margin-top: 14px;
  }
  .card--front .brand-name { color: var(--card-white); font-size: 54px; text-align: center; }
  .card--front .brand-tagline { color: var(--card-white); font-size: 22px; letter-spacing: 9px; }
  .card--back .brand-name { color: var(--ink-navy); font-size: 42px; }
  .card--back .brand-tagline { color: var(--ink-navy); font-size: 17px; letter-spacing: 5px; }
  .name-line { display: block; white-space: nowrap; }
  .divider {
    width: 2px; height: 230px;
    background: var(--rule);
    margin: 0 32px 0 30px;
    flex: none;
  }
  .contact-list { list-style: none; display: flex; flex-direction: column; gap: 12px; }
  .contact-item {
    display: flex; align-items: flex-start; gap: 12px;
    color: var(--ink-text);
    font-weight: 500; font-size: 18px; line-height: 1.3;
    white-space: nowrap;
  }
  .contact-icon { width: 20px; height: 20px; flex: none; margin-top: 2px; }
</style>
</head>
<body>
<main class="sheet">
  <section class="card card--front" aria-label="Card front">
    <div class="brand">
      <p class="brand-name">Martin K. Hollis</p>
      <p class="brand-tagline">Injury Lawyer</p>
    </div>
  </section>

  <section class="card card--back" aria-label="Card back">
    <div class="brand">
      <p class="brand-name"><span class="name-line">Martin K.</span><span class="name-line">Hollis</span></p>
      <p class="brand-tagline">Injury Lawyer</p>
    </div>
    <div class="divider"></div>
    <ul class="contact-list">
      <li class="contact-item">
        <svg class="contact-icon" viewBox="0 0 24 24" fill="var(--icon-blue)" aria-hidden="true">
          <path d="M6.6 10.8a15 15 0 0 0 6.6 6.6l2.2-2.2a1 1 0 0 1 1-.25 11.4 11.4 0 0 0 3.6.57 1 1 0 0 1 1 1V20a1 1 0 0 1-1 1A17 17 0 0 1 3 4a1 1 0 0 1 1-1h3.5a1 1 0 0 1 1 1c0 1.25.2 2.45.57 3.6a1 1 0 0 1-.25 1z"/>
        </svg>
        401-627-4193
      </li>
      <li class="contact-item">
        <svg class="contact-icon" viewBox="0 0 24 24" aria-hidden="true">
          <path d="M2 5h20v14H2z" fill="var(--icon-blue)"/>
          <path d="M2 5l10 8 10-8" fill="none" stroke="#fff" stroke-width="1.6"/>
        </svg>
        Martin@martinhollis.com
      </li>
      <li class="contact-item">
        <svg class="contact-icon" viewBox="0 0 24 24" fill="none" stroke="var(--icon-blue)" stroke-width="1.6" aria-hidden="true">
          <circle cx="12" cy="12" r="9.5"/>
          <ellipse cx="12" cy="12" rx="4.2" ry="9.5"/>
          <path d="M2.5 12h19M4 7h16M4 17h16"/>
        </svg>
        Martinhollis.com
      </li>
      <li class="contact-item">
        <svg class="contact-icon" viewBox="0 0 24 24" fill="var(--icon-blue)" aria-hidden="true">
          <path d="M12 2a7 7 0 0 0-7 7c0 5.2 7 13 7 13s7-7.8 7-13a7 7 0 0 0-7-7zm0 9.5A2.5 2.5 0 1 1 12 6.5a2.5 2.5 0 0 1 0 5z"/>
        </svg>
        <span>The Corvell Building<br>718 Tandy Street<br>Providence, RI 02908</span>
      </li>
    </ul>
  </section>
</main>
</body>
</html>
```